Corporate Branding - Web and Print

A UK based company will like to use an existing logo to create branding materials for all marketing related documents, including business card, prints, letterhead, Website, Twitter, Facebook, Instagram logo etc. This company serves high-end clientele in the fashion, health and wellness and as such high quality and class is of utmost importance.
Where the logo can be modernised without losing its character then experiment. The main thing is to have a corporate branding which can be used later for brochures, Business Plan infographics.
The prominent colour within the organisation is burnt orange with no secondary colour. However if you believe a secondary colour is needed then use it, otherwise keep it simple and classy. Any chosen colours have to match perfectly.
Target Market(s)
High net worth individuals
Industry/Entity Type
Health And Wellness
Contact Information for Business Card
classy

```html
<!DOCTYPE html>
<html lang="en">
<head>
<meta charset="utf-8">
<title>Ravelle — Business Card</title>
<link rel="stylesheet" href="https://fonts.googleapis.com/css2?family=Lato:wght@400;700;900&display=swap">
<style>
  :root {
    --burnt-orange: #e8870f;
    --orange-deep: #d97706;
    --orange-light: #f59a21;
    --card-white: #f7f7f7;
    --ink-grey: #5a5a5a;
    --ink-dark: #3f3f3f;
    --backdrop: #2b2b2b;
  }
  * { box-sizing: border-box; margin: 0; padding: 0; }
  html, body {
    width: 1200px; height: 873px; overflow: hidden;
    background: var(--backdrop);
    font-family: "Lato", sans-serif;
  }
  .stage {
    position: relative; width: 1200px; height: 873px;
    display: flex; align-items: center; justify-content: center; gap: 60px;
  }
  .card {
    position: relative; width: 520px; height: 297px; overflow: hidden;
    border-radius: 2px;
  }

  /* Front */
  .card-front { display: flex; align-items: center; justify-content: center; }
  .front-texture {
    position: absolute; inset: 0;
    background: linear-gradient(135deg, var(--orange-light) 0%, var(--burnt-orange) 50%, var(--orange-deep) 100%);
  }
  .brand {
    position: relative; display: flex; align-items: center; gap: 12px;
    font-weight: 900; letter-spacing: 2px; text-transform: uppercase;
  }
  .brand-dot { border-radius: 50%; flex: none; }
  .card-front .brand { color: #ffffff; font-size: 54px; }
  .card-front .brand-dot { width: 40px; height: 40px; background: #ffffff; }

  /* Back */
  .card-back { background: var(--card-white); }
  .card-back .brand {
    position: absolute; top: 52px; left: 0; right: 0; justify-content: center;
    color: var(--burnt-orange); font-size: 40px;
  }
  .card-back .brand-dot { width: 30px; height: 30px; background: var(--burnt-orange); }
  .holder { position: absolute; left: 42px; top: 160px; }
  .holder-name { color: var(--burnt-orange); font-weight: 700; font-size: 19px; }
  .holder-role { color: var(--ink-grey); font-size: 18px; margin-top: 2px; }
  .divider {
    position: absolute; left: 268px; top: 138px; width: 2px; height: 64px;
    background: linear-gradient(to bottom, transparent, var(--burnt-orange), transparent);
  }
  .contacts { position: absolute; left: 292px; top: 134px; list-style: none; }
  .contacts li {
    display: flex; align-items: center; gap: 12px;
    color: var(--ink-dark); font-size: 15px; line-height: 23px;
  }
  .contacts svg { width: 13px; height: 13px; fill: var(--burnt-orange); flex: none; }
  .accent-stripe {
    position: absolute; left: 0; right: 0; bottom: 66px; height: 8px;
    background: var(--burnt-orange);
  }
  .footer-band {
    position: absolute; left: 0; right: 0; bottom: 0; height: 46px;
    background: var(--burnt-orange);
    display: flex; align-items: center; justify-content: center;
    color: #ffffff; font-weight: 700; font-size: 17px; letter-spacing: 3px;
  }
</style>
</head>
<body>
<main class="stage">
  <section class="card card-front">
    <div class="front-texture" role="img" aria-label="Faceted low-poly orange background texture"></div>
    <div class="brand"><span class="brand-dot"></span>Ravelle</div>
  </section>

  <section class="card card-back">
    <div class="brand"><span class="brand-dot"></span>Ravelle</div>

    <div class="holder">
      <p class="holder-name">Mira Holt</p>
      <p class="holder-role">Speech Pathologist</p>
    </div>

    <div class="divider"></div>

    <ul class="contacts">
      <li>
        <svg viewBox="0 0 16 16" aria-hidden="true"><path d="M3 1h3l1.5 4-2 1.5a9 9 0 0 0 4 4L11 8.5l4 1.5v3a2 2 0 0 1-2 2A12 12 0 0 1 1 3a2 2 0 0 1 2-2z"/></svg>
        0400 123 456
      </li>
      <li>
        <svg viewBox="0 0 16 16" aria-hidden="true"><path d="M4 1h8v4H4zM1 6h14v6h-3v3H4v-3H1zM5 10v3h6v-3z"/></svg>
        003-555-0192
      </li>
      <li>
        <svg viewBox="0 0 16 16" aria-hidden="true"><path d="M1 3h14v10H1zM2.5 4.5 8 9l5.5-4.5z" fill-rule="evenodd"/></svg>
        mira@voicehaven.com.au
      </li>
    </ul>

    <div class="accent-stripe"></div>
    <div class="footer-band">www.ravelle.com</div>
  </section>
</main>
</body>
</html>
```